Business card for utility of the future

I need a business card template designed for brivolo. We provide sustainable water, energy and waste services to homes.

The card should include name, position, email address, phone number, website and our logo (attached). I would like it to convey professionalism and creativity.

Target Market(s)

Homeowners, investors, corporate partners.

Industry/Entity Type

Utility

Contact Information for Business Card

The card should include name, position, email address, phone number, website and our logo (attached).

```html
<!DOCTYPE html>
<html lang="en">
<head>
<meta charset="UTF-8">
<title>brivolo business card</title>
<link rel="stylesheet" href="https://fonts.googleapis.com/css2?family=Montserrat:wght@500;700&family=Poppins:wght@600;700&display=swap">
<style>
  :root {
    --backdrop: #2b2b2d;
    --leaf: #66bd7f;
    --coral: #f08a67;
    --ink: #050505;
    --paper: #ffffff;
  }
  html, body {
    margin: 0;
    width: 1200px;
    height: 900px;
    overflow: hidden;
    background: var(--backdrop);
  }
  .stage {
    position: relative;
    width: 1200px;
    height: 900px;
  }
  .card {
    position: absolute;
    width: 665px;
    height: 380px;
    overflow: hidden;
    box-shadow: 0 18px 40px rgba(0,0,0,0.45);
  }
  .card svg.shapes {
    position: absolute;
    inset: 0;
  }
  .card-front {
    left: 110px;
    top: 55px;
    background: var(--leaf);
  }
  .card-back {
    left: 425px;
    top: 465px;
    background: var(--ink);
  }
  .wordmark {
    position: absolute;
    font-family: "Poppins", sans-serif;
    font-weight: 700;
    letter-spacing: -2px;
    line-height: 1;
    display: flex;
    align-items: center;
    gap: 10px;
  }
  .wordmark .dot {
    width: 16px;
    height: 16px;
    border-radius: 50%;
    background: var(--coral);
  }
  .card-front .wordmark {
    left: 170px;
    top: 120px;
    font-size: 96px;
    color: var(--paper);
  }
  .card-back .wordmark {
    left: 45px;
    top: 92px;
    font-size: 78px;
    color: var(--leaf);
  }
  .front-url {
    position: absolute;
    right: 40px;
    top: 282px;
    font-family: "Montserrat", sans-serif;
    font-weight: 700;
    font-size: 15px;
    color: var(--paper);
    letter-spacing: 0.3px;
  }
  .person {
    position: absolute;
    right: 40px;
    top: 58px;
    text-align: right;
    font-family: "Montserrat", sans-serif;
  }
  .person-name {
    font-weight: 700;
    font-size: 20px;
    letter-spacing: 2px;
    color: var(--coral);
    text-transform: uppercase;
  }
  .person-role {
    font-weight: 500;
    font-size: 15px;
    color: var(--leaf);
    margin-top: 2px;
  }
  .contacts {
    position: absolute;
    left: 45px;
    top: 262px;
    margin: 0;
    padding: 0;
    list-style: none;
    font-family: "Montserrat", sans-serif;
    font-weight: 500;
    font-size: 17px;
    color: var(--leaf);
  }
  .contacts li {
    display: flex;
    align-items: center;
    gap: 10px;
    height: 24px;
  }
  .contacts svg {
    width: 13px;
    height: 13px;
    flex: none;
  }
</style>
</head>
<body>
<main class="stage">

  <section class="card card-front" aria-label="Card front">
    <svg class="shapes" viewBox="0 0 665 380" width="665" height="380" aria-hidden="true">
      <polygon points="0,322 360,322 400,342 0,342" fill="var(--paper)"/>
      <rect x="0" y="342" width="665" height="38" fill="var(--paper)"/>
      <polygon points="400,342 430,342 430,380 400,380" fill="var(--paper)"/>
      <polygon points="440,330 458,330 452,342 434,342" fill="var(--coral)"/>
      <polygon points="464,330 482,330 476,342 458,342" fill="var(--coral)"/>
      <polygon points="490,318 665,304 665,318 484,332" fill="var(--coral)"/>
      <polygon points="430,342 665,318 665,380 430,380" fill="var(--leaf)"/>
    </svg>
    <div class="wordmark">brivolo<span class="dot"></span></div>
    <div class="front-url">www.livewellnest.com</div>
  </section>

  <section class="card card-back" aria-label="Card back">
    <svg class="shapes" viewBox="0 0 665 380" width="665" height="380" aria-hidden="true">
      <line x1="410" y1="112" x2="625" y2="112" stroke="var(--coral)" stroke-width="1.5"/>
      <line x1="45" y1="250" x2="330" y2="250" stroke="var(--coral)" stroke-width="1.5"/>
      <polygon points="0,352 440,352 430,365 0,365" fill="var(--coral)"/>
      <polygon points="450,336 470,336 462,352 442,352" fill="var(--coral)"/>
      <polygon points="476,336 496,336 488,352 468,352" fill="var(--coral)"/>
      <polygon points="510,320 550,320 542,336 502,336" fill="var(--leaf)"/>
      <polygon points="565,262 665,262 665,380 560,380 560,300" fill="var(--leaf)"/>
    </svg>
    <div class="wordmark">brivolo<span class="dot"></span></div>
    <div class="person">
      <div class="person-name">Dana Reyes</div>
      <div class="person-role">Director</div>
    </div>
    <ul class="contacts">
      <li>
        <svg viewBox="0 0 24 24" aria-label="Phone"><path fill="var(--coral)" d="M6.6 10.8a15 15 0 0 0 6.6 6.6l2.2-2.2c.3-.3.7-.4 1-.2 1.1.4 2.3.6 3.6.6.6 0 1 .4 1 1V20c0 .6-.4 1-1 1A17 17 0 0 1 3 4c0-.6.4-1 1-1h3.5c.6 0 1 .4 1 1 0 1.3.2 2.5.6 3.6.1.3 0 .7-.2 1z"/></svg>
        (503) 555-0142
      </li>
      <li>
        <svg viewBox="0 0 24 24" aria-label="Email"><rect x="2" y="5" width="20" height="14" rx="1.5" fill="none" stroke="var(--coral)" stroke-width="2"/><path d="M3 6l9 7 9-7" fill="none" stroke="var(--coral)" stroke-width="2"/></svg>
        hello@livewellnest.com
      </li>
      <li>
        <svg viewBox="0 0 24 24" aria-label="Website"><circle cx="12" cy="12" r="9" fill="none" stroke="var(--coral)" stroke-width="2"/><path d="M3 12h18M12 3c3 3 3 15 0 18M12 3c-3 3-3 15 0 18" fill="none" stroke="var(--coral)" stroke-width="1.6"/></svg>
        www.livewellnest.com
      </li>
    </ul>
  </section>

</main>
</body>
</html>
```